" A empresa em questao será uma clínica médica e de fisioterapia especializada em tratamento de coluna. Tanto os médicos quanto os tratamentos fisioterápicos (fisioterapia, osteopatia, RPG) serao direcionados para o público que busca tratamento e soluçoes para dores nas costas em geral. "

```html
<!DOCTYPE html>
<html lang="pt-BR">
<head>
<meta charset="utf-8">
<title>Instituto Eixo Vital — Envelope</title>
<link rel="stylesheet" href="https://fonts.googleapis.com/css2?family=Cinzel:wght@400&family=Open+Sans:wght@400&display=swap">
<style>
  :root {
    --backdrop: #e9e6e1;
    --paper: #ffffff;
    --ink: #0b0b0b;
    --ring-light: #cfcfcf;
    --ring-mid: #a3a3a3;
    --ring-dark: #8a8a8a;
    --text-light: #ffffff;
    --text-dark: #3a3a3a;
  }
  * { margin: 0; padding: 0; box-sizing: border-box; }
  html, body {
    width: 1200px;
    height: 1200px;
    overflow: hidden;
    background: var(--backdrop);
  }
  .stage {
    position: relative;
    width: 1200px;
    height: 1200px;
  }
  .envelope {
    position: absolute;
    top: 240px;
    width: 462px;
    height: 672px;
    overflow: hidden;
    box-shadow: 0 6px 18px rgba(0,0,0,0.18);
  }
  .envelope--back {
    left: 126px;
    background: var(--paper);
  }
  .envelope--front {
    left: 619px;
    background: var(--ink);
  }
  .ring-art {
    position: absolute;
    left: 0;
    top: 0;
    width: 462px;
    height: 672px;
    display: block;
  }
  .flap {
    position: absolute;
    top: 0;
    left: 0;
    width: 100%;
    height: 94px;
    background: var(--ink);
    border-radius: 0 0 30px 30px;
  }
  .return-address {
    position: absolute;
    left: 28px;
    top: 624px;
    font-family: "Open Sans", sans-serif;
    font-size: 8px;
    line-height: 1.55;
    color: var(--text-dark);
  }
  .brand {
    position: absolute;
    left: 182px;
    top: 548px;
    display: flex;
    align-items: center;
  }
  .brand__dot {
    width: 40px;
    height: 40px;
    border: 2px solid var(--text-light);
    border-radius: 50%;
    flex: none;
    margin-right: 16px;
  }
  .brand__name {
    border-left: 1px solid var(--text-light);
    padding-left: 12px;
    font-family: "Cinzel", serif;
    font-weight: 400;
    color: var(--text-light);
    font-size: 26px;
    line-height: 1.08;
  }
  .brand__name span { display: block; }
  .brand__name .brand__lead {
    font-size: 13px;
    letter-spacing: 3px;
    line-height: 1.4;
  }
</style>
</head>
<body>
  <main class="stage">
    <section class="envelope envelope--back">
      <svg class="ring-art" viewBox="0 0 462 672" aria-hidden="true">
        <defs>
          <linearGradient id="backRing" x1="0" y1="0" x2="1" y2="1">
            <stop offset="0" stop-color="#9e9e9e"/>
            <stop offset="0.55" stop-color="#b5b5b5"/>
            <stop offset="0.9" stop-color="#f4f4f4"/>
          </linearGradient>
        </defs>
        <circle cx="362" cy="355" r="240" fill="none" stroke="url(#backRing)" stroke-width="34"/>
      </svg>
      <div class="flap"></div>
      <p class="return-address">
        Rua das Palmeiras, 120 Bairro Centro<br>
        Cidade Nova - Cep 00.000-000
      </p>
    </section>

    <section class="envelope envelope--front">
      <svg class="ring-art" viewBox="0 0 462 672" aria-hidden="true">
        <defs>
          <linearGradient id="frontRing" x1="0" y1="0" x2="0" y2="1">
            <stop offset="0" stop-color="#c9c9c9"/>
            <stop offset="0.5" stop-color="#a8a8a8"/>
            <stop offset="1" stop-color="#8d8d8d"/>
          </linearGradient>
        </defs>
        <circle cx="0" cy="372" r="240" fill="#ffffff"/>
        <circle cx="0" cy="372" r="240" fill="none" stroke="url(#frontRing)" stroke-width="34"/>
      </svg>
      <div class="brand">
        <span class="brand__dot" aria-hidden="true"></span>
        <p class="brand__name">
          <span class="brand__lead">Instituto</span>
          <span>Eixo Vital</span>
        </p>
      </div>
    </section>
  </main>
</body>
</html>
```